Front and back cover design for skincare marketing materials

Thank you for showing an interest in my project.
Project Details.

I require a front and back cover for our marketing materials.
·       Front Cover size: 105 mm W x 150 mm H.
·       Back Cover size:  105 mm W x 150 mm H.
·       It must include these two colors. You can use a third color if you wish.
1.     #DBA09D
2.     #FFFFFF
 
Front Cover
·      The front cover will have a faded image of the Kakadu Plum branch and fruit. There are two image files, KP_image-1.jpg and kp_image-2.jpeg. You can use both images, just a portion of them, or source alternative royalty-free images of Kakadu Plum that may better fit the design. These two files have been uploaded.
 
The front cover wording.
Top of the front cover.
a.     The title of the image. “Kakadu Plum”
b.     The brand name, “Velora Skincare”. The file brand_name.ai uploaded.
 
Bottom of the front cover- Designer's choice of font.
The bottom of the front cover contains three lines of text in the following order.  
1.     Australian Native Ingredients
2.     100% Natural · Organic · Wild-harvested
3.     Australian-Made Premium Skincare
 
Back Cover
·      Back Cover wording.The back cover contains the following words "grown by nature" in white (#FFFFFF) of font Italianno (font_file.ttf) with a background color of #DBA09D as seen in the sample box (sample_box.pdf) right-side panel
 
Please provide one file for the front cover and a separate file for the back cover.
All the elements of the files must be editable.
 
Do NOT use the Curve function on the files, as the text must remain editable/changeable.
 
All assets/resources/files, including fonts not supplied by us but used by the designer, must be named and provided with the finished design.
Updates

Slow to provide project details.

Target Market(s)

Beauty-minded Asian consumers between the ages of 32 and 75 who take a proactive approach to maintaining younger-looking skin. Those who already know the danger of skin damage caused by skincare containing harsh chemicals choose effective natural/organic solutions to meet their skincare needs. Those who wish a more radiant glow and youthful appearance to their skin. Usually, a two-income middle to high-income bracket couples with a mindset for health and beauty.

Industry/Entity Type

beauty

Font styles to use
Other font styles liked:
• I will provide a font file and a brand name file.

Requirements
Must have
• You must use the two colors provided on the product box. The designer may use a third color.
Nice to have
• some gold colour

```html
<!DOCTYPE html>
<html lang="en">
<head>
<meta charset="utf-8">
<title>Velora Skincare – Kakadu Plum Cover Spread</title>
<link href="https://fonts.googleapis.com/css2?family=Italianno&family=Quicksand:wght@500&family=Lato:wght@400&display=swap" rel="stylesheet">
<style>
  :root {
    --rose: #DBA09D;
    --white: #FFFFFF;
    --page: #FFFFFF;
    --ink: #4a4740;
    --leaf-light: #e9e39a;
    --leaf-mid: #c9cf7a;
    --leaf-sage: #b6c79a;
    --leaf-olive: #a9ae55;
    --fruit: #c2c48a;
  }
  * { margin: 0; padding: 0; box-sizing: border-box; }
  html, body {
    width: 1200px; height: 1090px; overflow: hidden;
    background: var(--page);
  }
  .canvas { position: relative; width: 1200px; height: 1090px; }

  .spread {
    position: absolute; left: 71px; top: 162px;
    width: 1014px; height: 724px;
    display: flex;
  }
  .panel { position: relative; width: 253.5px; height: 100%; overflow: hidden; }

  .panel--photo {
    background:
      radial-gradient(ellipse 60% 30% at 30% 25%, rgba(182,199,154,0.9), transparent 70%),
      radial-gradient(ellipse 70% 25% at 50% 60%, rgba(220,200,130,0.8), transparent 70%),
      linear-gradient(180deg, #d9d39a 0%, #d8cf98 30%, #cdbf7f 55%, #bdb86a 80%, #c3c25a 100%);
  }

  .panel--tagline { background: var(--rose); }
  .tagline {
    position: absolute; left: 50%; top: 50%;
    transform: translate(-50%, -50%) rotate(-90deg);
    font-family: "Italianno", cursive;
    font-size: 106px; line-height: 1;
    color: var(--white); white-space: nowrap;
  }

  .panel--front {
    background:
      radial-gradient(ellipse 50% 25% at 15% 30%, rgba(182,199,154,0.85), transparent 70%),
      radial-gradient(ellipse 60% 30% at 80% 45%, rgba(233,200,140,0.6), transparent 70%),
      linear-gradient(180deg, var(--leaf-light) 0%, #dfe0a0 18%, #d2cf8a 45%, var(--leaf-mid) 70%, var(--leaf-olive) 100%);
  }
  .front__title {
    position: absolute; left: 0; right: 0; top: 45px;
    text-align: center;
    font-family: "Quicksand", sans-serif; font-weight: 500;
    font-size: 43px; line-height: 58px;
    color: var(--white);
  }
  .front__brand {
    position: absolute; left: 0; right: 0; top: 202px;
    text-align: center;
    font-family: "Quicksand", sans-serif; font-weight: 500;
    font-size: 24px; letter-spacing: 1px;
    color: var(--rose);
  }
  .front__fruit {
    position: absolute; left: 24px; top: 298px;
    width: 212px; height: 232px;
    border-radius: 45% 50% 40% 50%;
    background: radial-gradient(ellipse at 50% 50%, var(--fruit) 0%, rgba(194,196,138,0.75) 45%, rgba(194,196,138,0) 72%);
  }
  .front__claims {
    position: absolute; left: 14px; top: 618px;
    list-style: none;
    font-family: "Lato", sans-serif; font-size: 11.5px; line-height: 17px;
    color: var(--ink);
  }
  .front__claims li::before { content: "- "; padding-right: 3px; }
</style>
</head>
<body>
<main class="canvas">
  <section class="spread">
    <div class="panel panel--photo" role="img" aria-label="Soft-focus photograph of Kakadu Plum foliage and fruit"></div>

    <div class="panel panel--tagline">
      <p class="tagline">grown by nature</p>
    </div>

    <div class="panel panel--front" role="group" aria-label="Front cover">
      <h1 class="front__title">Kakadu<br>Plum</h1>
      <p class="front__brand">Velora Skincare</p>
      <div class="front__fruit" role="img" aria-label="Photograph of a Kakadu Plum branch with four green fruits"></div>
      <ul class="front__claims">
        <li>Australian Native Ingredients</li>
        <li>100% Natural · Organic · Wild-harvested</li>
        <li>Australian-Made Premium Skincare</li>
      </ul>
    </div>

    <div class="panel panel--tagline">
      <p class="tagline">grown by nature</p>
    </div>
  </section>
</main>
</body>
</html>
```